VELMARKS COFFEE CUPS

I WANT A DESIGN FOR TAKE AWAY COFFEE CUPS 12 oz. IN THE ATTACHED PROFILES YOU'LL FIND THE LOGO AND SOME DESIGNS I LIKE (WHICH IS FLOWER OR COFFEE QOUTES) THE COLORS ARE PREFERLY WHITE, PINK, PURPLE OR YOU CAN DO OTHER COLORS IF NICER.

```html
<!DOCTYPE html>
<html lang="en">
<head>
<meta charset="UTF-8">
<title>Velmarks Coffee Cup Wrap</title>
<link href="https://fonts.googleapis.com/css2?family=Petit+Formal+Script&family=Ubuntu:wght@400;700&display=swap" rel="stylesheet">
<style>
  :root {
    --page: #ffffff;
    --wrap-purple: #4e5299;
    --ink-white: #ffffff;
    --logo-gold: #d3a86a;
    --logo-frame: #e36a9a;
    --logo-ink: #4a2a1a;
    --petal-pink: #e7879f;
    --petal-pink-light: #f9dbe4;
    --petal-white: #fbf8f8;
    --petal-white-shade: #ddd6dd;
    --petal-lilac: #b697dc;
    --petal-lilac-light: #efe4f8;
    --petal-violet: #8a66c2;
  }
  * { box-sizing: border-box; margin: 0; padding: 0; }
  html, body { width: 1200px; height: 1200px; overflow: hidden; background: var(--page); }
  .canvas { position: relative; width: 1200px; height: 1200px; }

  .cup-wrap {
    position: absolute; left: 40px; top: 320px;
    width: 1120px; height: 560px;
    background: var(--wrap-purple);
    overflow: hidden;
  }

  .flower { position: absolute; }
  .flower--pink-top {
    left: 440px; top: -20px; width: 160px; height: 215px;
    border-radius: 62% 38% 55% 45% / 40% 58% 42% 60%;
    background: radial-gradient(ellipse at 55% 40%, var(--petal-pink-light) 0%, var(--petal-pink) 55%, rgba(231,135,159,0) 72%);
  }
  .flower--white-top {
    left: 560px; top: -40px; width: 400px; height: 270px;
    border-radius: 45% 55% 62% 38% / 35% 45% 55% 65%;
    background: radial-gradient(ellipse at 50% 40%, var(--petal-white) 0%, var(--petal-white) 30%, var(--petal-white-shade) 58%, rgba(221,214,221,0) 72%);
  }
  .flower--lilac-top {
    left: 840px; top: -30px; width: 310px; height: 330px;
    border-radius: 38% 62% 40% 60% / 55% 45% 60% 40%;
    background: radial-gradient(ellipse at 50% 45%, var(--petal-lilac-light) 0%, var(--petal-lilac) 45%, var(--petal-violet) 62%, rgba(138,102,194,0) 74%);
  }
  .flower--pink-bottom {
    left: -40px; top: 300px; width: 360px; height: 300px;
    border-radius: 55% 45% 38% 62% / 48% 60% 40% 52%;
    background: radial-gradient(ellipse at 50% 50%, var(--petal-pink-light) 0%, var(--petal-pink) 50%, rgba(231,135,159,0) 72%);
  }
  .flower--violet-bottom {
    left: 250px; top: 360px; width: 370px; height: 240px;
    border-radius: 60% 40% 45% 55% / 52% 38% 62% 48%;
    background: radial-gradient(ellipse at 50% 55%, var(--petal-lilac-light) 0%, var(--petal-lilac) 45%, var(--petal-violet) 62%, rgba(138,102,194,0) 74%);
  }
  .flower--white-bottom {
    left: 655px; top: 295px; width: 180px; height: 220px;
    border-radius: 42% 58% 50% 50% / 60% 40% 60% 40%;
    background: radial-gradient(ellipse at 50% 50%, var(--petal-white) 0%, var(--petal-white) 30%, var(--petal-white-shade) 55%, rgba(221,214,221,0) 72%);
  }

  .quote {
    position: absolute; left: 70px; top: 40px; width: 280px;
    text-align: center; color: var(--ink-white);
    font-family: "Petit Formal Script", cursive;
    font-size: 32px; line-height: 53px; font-weight: 400;
  }
  .quote__mark { display: block; font-size: 56px; line-height: 44px; }
  .quote__tilde { display: block; font-size: 24px; line-height: 20px; }

  .logo-panel {
    position: absolute; left: 370px; top: 185px;
    width: 381px; height: 188px;
    border: 3px solid var(--logo-frame);
    background: var(--page);
    padding: 5px;
  }
  .logo-panel__inner {
    width: 100%; height: 100%;
    background: var(--logo-gold);
    display: flex; align-items: center; justify-content: center;
  }
  .brand-name {
    font-family: "Ubuntu", sans-serif; font-weight: 700;
    font-size: 56px; letter-spacing: 2px; color: var(--logo-ink);
  }

  .menu-list {
    position: absolute; left: 853px; top: 284px;
    list-style: none;
    font-family: "Ubuntu", sans-serif; font-size: 20px;
    color: var(--ink-white); letter-spacing: 1px;
  }
  .menu-list__item { display: flex; align-items: center; height: 43.5px; }
  .menu-list__box {
    width: 29px; height: 29px; border: 1.5px solid var(--ink-white);
    margin-right: 19px; flex: none;
  }
</style>
</head>
<body>
<main class="canvas">
  <section class="cup-wrap">
    <div class="flower flower--pink-top" role="img" aria-label="Pink peony illustration"></div>
    <div class="flower flower--white-top" role="img" aria-label="White peony illustration"></div>
    <div class="flower flower--lilac-top" role="img" aria-label="Lilac peony illustration"></div>
    <div class="flower flower--pink-bottom" role="img" aria-label="Pink peony illustration"></div>
    <div class="flower flower--violet-bottom" role="img" aria-label="Violet peony illustration"></div>
    <div class="flower flower--white-bottom" role="img" aria-label="White carnation illustration"></div>

    <p class="quote">
      <span class="quote__mark">&ldquo;</span>
      You call it<br>addiction
      <span class="quote__tilde">~</span>
      I prefer<br>love
    </p>

    <div class="logo-panel">
      <div class="logo-panel__inner">
        <span class="brand-name">VELMARKS</span>
      </div>
    </div>

    <ul class="menu-list">
      <li class="menu-list__item"><span class="menu-list__box"></span>Cafe Latté</li>
      <li class="menu-list__item"><span class="menu-list__box"></span>Capuchino</li>
      <li class="menu-list__item"><span class="menu-list__box"></span>Americano</li>
      <li class="menu-list__item"><span class="menu-list__box"></span>Cafe Mocha</li>
      <li class="menu-list__item"><span class="menu-list__box"></span>ETC</li>
    </ul>
  </section>
</main>
</body>
</html>
```